Brimvane.com fiber optic internet website redesign

We need a new website design for our fiber optic internet company that provides internet, phone, and tv services. It should use the text "Marrowfen fiber optics", and "I beamed up with Marrowfen". The design should use the color blue and the attached logo.
We are a 30 year old internet company who started as a dial up internet provider in our basement. Today we design, build, and maintain our own fiber optic internet network to provide service to residential, business, educational, healthcare, and governmental customers

```html
<!DOCTYPE html>
<html lang="en">
<head>
<meta charset="utf-8">
<title>Brimvane — Marrowfen Fiber Optics</title>
<link rel="stylesheet" href="https://fonts.googleapis.com/css2?family=Plus+Jakarta+Sans:wght@400;500;600;700;800&display=swap">
<style>
:root{
  --blue:#0d4fa8;
  --blue-dark:#0a3f8c;
  --navy:#07173a;
  --ink:#111317;
  --muted:#4a4f58;
  --line:#e4e7ec;
  --soft:#f5f6f8;
  --white:#ffffff;
}
*{box-sizing:border-box;margin:0;padding:0}
html,body{width:1200px;height:4107px;overflow:hidden}
body{font-family:"Plus Jakarta Sans",sans-serif;color:var(--ink);background:var(--white);position:relative}
.abs{position:absolute}
svg{display:block}

/* nav */
.nav{left:0;top:0;width:1200px;height:85px;background:var(--white);border-bottom:1px solid var(--line)}
.brand{display:flex;align-items:center;gap:8px;font-weight:700;font-size:28px;color:var(--ink)}
.brand .dot{width:34px;height:34px;border-radius:50%;background:var(--blue)}
.nav .brand{left:134px;top:24px}
.nav-links{left:310px;top:33px;display:flex;gap:0;font-size:15px;font-weight:500}
.nav-links span{position:absolute;white-space:nowrap}
.btn{display:inline-flex;align-items:center;justify-content:center;border-radius:5px;font-weight:700}
.btn-solid{background:var(--blue);color:var(--white)}
.btn-outline{border:1.5px solid var(--blue);color:var(--blue);background:var(--white)}
.nav .btn{left:952px;top:26px;width:115px;height:35px;font-size:14px;gap:10px}

/* hero */
.hero{left:0;top:85px;width:1200px;height:530px;background:var(--soft)}
.media{border-radius:10px}
.hero h1{left:542px;top:138px;font-size:50px;line-height:60px;font-weight:700;width:620px}
.hero h1 em{font-style:normal;color:var(--blue)}
.hero .sub{left:542px;top:272px;font-size:18px;font-weight:500}
.tile{width:170px;height:155px;background:var(--white);border-radius:8px;box-shadow:0 6px 16px rgba(20,40,80,.08);display:flex;flex-direction:column;align-items:center;justify-content:flex-end;padding-bottom:18px;font-size:13px;font-weight:600}
.tile .corner{position:absolute;right:12px;top:12px;width:26px;height:26px;border-radius:50%;border:1.5px solid var(--blue);display:flex;align-items:center;justify-content:center}
.tile .ico{margin-bottom:14px}

/* services */
.icon-box{width:75px;height:75px;border-radius:8px;background:var(--white);box-shadow:0 4px 14px rgba(20,40,80,.1);display:flex;align-items:center;justify-content:center}
.svc h2{font-size:38px;font-weight:700;letter-spacing:-.5px;white-space:nowrap}
.svc p{font-size:17px;line-height:28px;width:460px}
.svc p.gap{margin-top:8px}
.svc .btn{height:38px;width:135px;font-size:17px;margin-top:24px}

/* features */
.feature{width:257px;height:293px;background:linear-gradient(#fff,#f3f6fb);border-radius:8px;box-shadow:0 4px 16px rgba(20,40,80,.08);padding:0 24px;text-align:center}
.feature .sq{width:95px;height:95px;margin:36px auto 20px;border-radius:6px;background:var(--blue);display:flex;align-items:center;justify-content:center}
.feature h3{font-size:17px;font-weight:700;margin-bottom:12px}
.feature ul{text-align:left;font-size:11.5px;color:var(--muted);line-height:16px;padding-left:14px}
.feature li{margin-bottom:8px}

/* about */
.section-title{width:1200px;text-align:center;font-size:38px;font-weight:700;color:var(--blue)}
.about-text{left:146px;top:3000px;width:480px;font-size:12.5px;line-height:16px;color:var(--muted)}
.about-text .years{display:flex;align-items:baseline;gap:10px;color:var(--ink);font-weight:600;font-size:14px;margin-bottom:22px}
.about-text .years b{font-size:38px;color:var(--blue);font-weight:800}
.about-text h4{color:var(--ink);font-size:14px;margin:16px 0 6px}

/* get started */
.start{left:0;top:3315px;width:1200px;height:491px;background:var(--soft)}
.start-card{width:330px;height:145px;background:var(--white);border-radius:8px;box-shadow:0 4px 16px rgba(20,40,80,.08);padding:24px 20px}
.start-card h3{display:flex;align-items:center;gap:10px;font-size:14px;font-weight:600;margin-bottom:16px}
.start-card ul{font-size:11px;line-height:15px;padding-left:10px}
.start-card b{font-weight:700}

/* footer */
.footer{left:0;top:3806px;width:1200px;height:301px;background:linear-gradient(110deg,var(--navy) 0%,#0b2d6e 55%,var(--blue) 100%);color:var(--white)}
.footer .brand{color:var(--white);left:134px;top:48px}
.footer .small{font-size:11px}
.contact-row{display:flex;align-items:center;gap:16px;font-size:10px}
.contact-row .pill{width:36px;height:36px;border-radius:6px;border:1.5px solid rgba(255,255,255,.5);background:rgba(255,255,255,.08);display:flex;align-items:center;justify-content:center}
.social{display:flex;gap:14px}
.social span{width:15px;height:15px;border-radius:50%;background:var(--white)}
</style>
</head>
<body>

<header class="abs nav">
  <div class="abs brand"><span class="dot"></span>brimvane</div>
  <nav class="abs nav-links">
    <span style="left:0">Home</span>
    <span style="left:85px">Services ⌄</span>
    <span style="left:210px">About</span>
    <span style="left:296px">Contact</span>
  </nav>
  <a class="abs btn btn-solid">Order Now <span>›</span></a>
</header>

<section class="abs hero">
  <div class="abs media" role="img" aria-label="City skyline with glowing blue fiber light streams" style="left:97px;top:30px;width:390px;height:475px;background:linear-gradient(160deg,#5fb2e6 0%,#1b5fa8 50%,#0b2f6a 100%)"></div>
  <h1 class="abs" style="top:53px">Get Lit with <em>Marrowfen</em><br>Fiber Optics</h1>
  <p class="abs sub" style="top:187px">Internet, Phone, and TV Services That Keep You Connected.</p>
  <a class="abs btn btn-solid" style="left:542px;top:248px;width:128px;height:46px;font-size:18px">Order Now</a>
  <a class="abs btn btn-outline" style="left:689px;top:248px;width:163px;height:46px;font-size:15px">Check Availability</a>

  <div class="abs tile" style="left:542px;top:350px">
    <span class="corner"><svg width="12" height="12" viewBox="0 0 12 12"><path d="M3 9 9 3M4 3h5v5" fill="none" stroke="#0d4fa8" stroke-width="1.5"/></svg></span>
    <svg class="ico" width="70" height="60" viewBox="0 0 70 60"><path d="M5 30 35 5l30 25M13 24v32h44V24" fill="none" stroke="#0d4fa8" stroke-width="4"/><rect x="27" y="36" width="16" height="20" fill="none" stroke="#0d4fa8" stroke-width="4"/></svg>
    Residential Services
  </div>
  <div class="abs tile" style="left:738px;top:350px">
    <span class="corner"><svg width="12" height="12" viewBox="0 0 12 12"><path d="M3 9 9 3M4 3h5v5" fill="none" stroke="#0d4fa8" stroke-width="1.5"/></svg></span>
    <svg class="ico" width="66" height="62" viewBox="0 0 66 62"><path d="M6 58h54M12 58V20l20-10v48M32 24h22v34" fill="none" stroke="#0d4fa8" stroke-width="4"/><path d="M20 32v4M26 32v4M20 44v4M26 44v4M42 36v4M42 46v4" stroke="#0d4fa8" stroke-width="4"/></svg>
    Business Services
  </div>
  <div class="abs tile" style="left:934px;top:350px">
    <span class="corner"><svg width="12" height="12" viewBox="0 0 12 12"><path d="M3 9 9 3M4 3h5v5" fill="none" stroke="#0d4fa8" stroke-width="1.5"/></svg></span>
    <svg class="ico" width="64" height="62" viewBox="0 0 64 62"><circle cx="32" cy="20" r="15" fill="none" stroke="#0d4fa8" stroke-width="4"/><circle cx="20" cy="40" r="15" fill="none" stroke="#0d4fa8" stroke-width="4"/><circle cx="44" cy="40" r="15" fill="none" stroke="#0d4fa8" stroke-width="4"/></svg>
    Packages
  </div>
</section>

<!-- internet -->
<section class="svc">
  <div class="abs icon-box" style="left:80px;top:712px"><svg width="44" height="34" viewBox="0 0 44 34"><path d="M3 12a28 28 0 0 1 38 0M9 19a19 19 0 0 1 26 0M15 26a10 10 0 0 1 14 0" fill="none" stroke="#0d4fa8" stroke-width="2.5" stroke-linecap="round"/><circle cx="22" cy="31" r="2" fill="#0d4fa8"/></svg></div>
  <h2 class="abs" style="left:80px;top:812px">High-Speed Internet</h2>
  <div class="abs" style="left:80px;top:868px">
    <p><b style="font-weight:700">Starting at $55/mo</b> for 25 Mbps download speeds.</p>
    <p class="gap" style="font-weight:600">Reliable, fast, and consistent for browsing, streaming, and more.</p>
    <p class="gap">No hidden fees or introductory surprises.</p>
    <a class="btn btn-outline">Learn More</a>
  </div>
  <div class="abs media" role="img" aria-label="Glowing blue fiber strands bending over a misty field" style="left:707px;top:716px;width:405px;height:339px;background:linear-gradient(180deg,#c7d4df 0%,#7c9ab3 55%,#2f5c8e 100%)"></div>
</section>

<!-- voip -->
<section class="svc">
  <div class="abs media" role="img" aria-label="Desk phone, smartphone, notepad and pen on a tiled surface" style="left:91px;top:1251px;width:405px;height:340px;background:linear-gradient(150deg,#e8edf3 0%,#b9c6d4 60%,#8c9db0 100%)"></div>
  <div class="abs icon-box" style="left:659px;top:1250px"><svg width="40" height="40" viewBox="0 0 40 40"><path d="M10 4 4 8c-1 12 14 28 28 28l4-6-7-5-4 3c-5-2-9-6-11-11l3-4z" fill="none" stroke="#0d4fa8" stroke-width="2.5" stroke-linejoin="round"/><path d="M24 6a10 10 0 0 1 10 10M24 12a4 4 0 0 1 4 4" fill="none" stroke="#0d4fa8" stroke-width="2.5" stroke-linecap="round"/></svg></div>
  <h2 class="abs" style="left:659px;top:1348px">VoIP Phone Service</h2>
  <div class="abs" style="left:659px;top:1404px">
    <p>Unlimited local and long-distance calling.</p>
    <p class="gap" style="font-weight:600">Keep your current number, with FREE voicemail and caller ID.</p>
    <p class="gap">Plans starting at <b>$25/mo.</b></p>
    <a class="btn btn-outline">Learn More</a>
  </div>
</section>

<!-- bundles -->
<section class="svc">
  <div class="abs icon-box" style="left:80px;top:1786px"><svg width="40" height="44" viewBox="0 0 40 44"><circle cx="20" cy="14" r="4" fill="none" stroke="#0d4fa8" stroke-width="2.5"/><path d="M10 22a12 12 0 1 1 20 0M20 18 10 42M20 18l10 24M13 34h14" fill="none" stroke="#0d4fa8" stroke-width="2.5" stroke-linecap="round"/></svg></div>
  <h2 class="abs" style="left:80px;top:1883px">Internet + Phone Bundles</h2>
  <div class="abs" style="left:80px;top:1939px">
    <p style="font-weight:600">Save money by combining your services.</p>
    <p class="gap">Internet + Phone starting at <b>$80/mo.</b></p>
    <p class="gap">One low monthly rate, one bill, zero hassle.</p>
    <a class="btn btn-outline">Learn More</a>
  </div>
  <div class="abs media" role="img" aria-label="Fiber optic cable with glowing light strands" style="left:707px;top:1786px;width:405px;height:312px;background:linear-gradient(135deg,#dce7f0 0%,#88aed0 50%,#3f77b0 100%)"></div>
</section>

<!-- features -->
<section>
  <div class="abs feature" style="left:179px;top:2375px">
    <div class="sq"><svg width="56" height="40" viewBox="0 0 56 40"><path d="M14 34a10 10 0 0 1 0-20 14 14 0 0 1 27-2 11 11 0 0 1 1 22z" fill="none" stroke="#fff" stroke-width="3"/><path d="M20 22l6 6 11-11" fill="none" stroke="#fff" stroke-width="3"/></svg></div>
    <h3>Reliable Fiber Network</h3>
    <ul><li>Built and operated by us—your local experts.</li><li>Faster, more stable than DSL or cable services.</li></ul>
  </div>
  <div class="abs feature" style="left:472px;top:2375px">
    <div class="sq"><svg width="48" height="46" viewBox="0 0 48 46"><path d="M8 28V22a16 16 0 0 1 32 0v6" fill="none" stroke="#fff" stroke-width="3"/><rect x="6" y="26" width="8" height="14" rx="3" fill="none" stroke="#fff" stroke-width="3"/><rect x="34" y="26" width="8" height="14" rx="3" fill="none" stroke="#fff" stroke-width="3"/><path d="M38 40c0 4-6 4-12 4" fill="none" stroke="#fff" stroke-width="3"/></svg></div>
    <h3>Local Customer Support</h3>
    <ul><li>We've been trusted since 1995.</li><li>When you call, we answer—no outsourcing!</li></ul>
  </div>
  <div class="abs feature" style="left:766px;top:2375px">
    <div class="sq"><svg width="54" height="36" viewBox="0 0 54 36"><path d="M3 5c16 6 32-6 48 0v26C35 25 19 37 3 31z" fill="none" stroke="#fff" stroke-width="3"/><circle cx="27" cy="18" r="5" fill="none" stroke="#fff" stroke-width="3"/><path d="M11 13v10M43 13v10" stroke="#fff" stroke-width="3"/></svg></div>
    <h3>Transparent Pricing</h3>
    <ul><li>No installation fees or hidden costs.</li><li>Free features like voicemail and caller ID included.</li></ul>
  </div>
</section>

<!-- about -->
<section>
  <h2 class="abs section-title" style="left:0;top:2823px">About Marrowfen</h2>
  <div class="abs about-text">
    <div class="years"><b>30</b>Years of Excellence</div>
    <p>Marrowfen started as a small dial-up provider in a basement in 1995. Today, we design, build, and maintain our own fiber optic network to serve homes, businesses, schools, healthcare, and government agencies.</p>
    <h4>Our Mission:</h4>
    <p>To deliver reliable, high-quality, and affordable communication services to our community.</p>
  </div>
  <div class="abs media" role="img" aria-label="Glowing blue digital globe with network connections" style="left:662px;top:2925px;width:393px;height:311px;border-radius:4px;background:radial-gradient(circle at 58% 58%,#9fdcff 0%,#2f8ad8 25%,#0d4a9a 60%,#0b2c66 100%)"></div>
</section>

<!-- get started -->
<section class="abs start">
  <h2 class="abs section-title" style="left:0;top:78px">How to Get Started</h2>
  <div class="abs start-card" style="left:261px;top:180px">
    <h3><svg width="34" height="28" viewBox="0 0 34 28"><path d="M2 14 17 2l15 12M6 11v15h22V11" fill="none" stroke="#0d4fa8" stroke-width="2.5"/><rect x="13" y="17" width="8" height="9" fill="none" stroke="#0d4fa8" stroke-width="2.5"/></svg>For Residential Customers</h3>
    <ul><li><b>Internet Services</b> for all your home needs.</li><li><b>Phone Plans</b> with unlimited calling.</li><li><b>Bundle Packages</b> for savings and convenience.</li></ul>
  </div>
  <div class="abs start-card" style="left:608px;top:180px">
    <h3><svg width="32" height="30" viewBox="0 0 32 30"><path d="M2 28h28M6 28V10l10-6v24M16 12h11v16" fill="none" stroke="#0d4fa8" stroke-width="2.5"/></svg>For Business Customers</h3>
    <ul><li><b>High-Speed Internet</b> to keep your team connected.</li><li><b>VoIP Phone Systems</b> for reliable communication.</li><li><b>Custom Bundles</b> designed for your business.</li></ul>
  </div>
  <a class="abs btn btn-solid" style="left:543px;top:377px;width:115px;height:38px;font-size:14px">Contact Us</a>
</section>

<!-- footer -->
<footer class="abs footer">
  <div class="abs brand"><span class="dot" style="background:#2b6fd0"></span>brimvane</div>
  <p class="abs small" style="left:134px;top:120px">I beamed up with Marrowfen</p>
  <p class="abs small" style="left:134px;top:158px;display:flex;gap:18px"><span>Services</span><span>About</span><span>Privacy</span><span>Terms</span></p>
  <div class="abs contact-row" style="left:613px;top:40px">
    <span class="pill"><svg width="18" height="18" viewBox="0 0 40 40"><path d="M10 4 4 8c-1 12 14 28 28 28l4-6-7-5-4 3c-5-2-9-6-11-11l3-4z" fill="none" stroke="#fff" stroke-width="3"/></svg></span>
    <span>Tel. 555.310.2046 &nbsp;&nbsp; Toll Free 1.800.555.0187</span>
  </div>
  <div class="abs contact-row" style="left:613px;top:96px">
    <span class="pill"><svg width="18" height="18" viewBox="0 0 20 20"><path d="M10 18s6-6 6-10a6 6 0 0 0-12 0c0 4 6 10 6 10z" fill="none" stroke="#fff" stroke-width="1.6"/><circle cx="10" cy="8" r="2" fill="#fff"/></svg></span>
    <span>48 Lantern Row - Ashdale, PA 10000</span>
  </div>
  <div class="abs" style="left:134px;top:220px;width:933px;height:1px;background:rgba(255,255,255,.3)"></div>
  <p class="abs small" style="left:134px;top:254px">© 2024 Brimvane. All rights reserved.</p>
  <div class="abs social" style="left:958px;top:254px"><span></span><span></span><span></span><span></span></div>
</footer>

</body>
</html>
```